Visitenkarten-Design für Commercial Expert
Zielgruppe
Guten Tag! Ich bin Single und suche neue sportliche Bekannte in der Nähe meines Wohnortes.
Aufgabenstellung
Dr. Mareike Venhaus
Commercial Expert
Telefonnummer 01762290471
Anschrift: Tulpenau 9, 24519 Birkenfelde
https://www.netzvelo-profil.de/profile/Mareike_Venhaus/

```html
<!DOCTYPE html>
<html lang="de">
<head>
<meta charset="utf-8">
<title>Visitenkarte – Dr. Mareike Venhaus</title>
<link rel="stylesheet" href="https://fonts.googleapis.com/css2?family=Roboto:ital,wght@0,400;0,500;1,400&display=swap">
<style>
  :root {
    --stage: #ecece8;
    --card-white: #ffffff;
    --lime: #c5f270;
    --lime-soft: #d2f68c;
    --leaf: #6b9a00;
    --icon: #7fb81c;
    --name-blue: #1a75bb;
    --ink: #1d2a3a;
    --muted: #4a5563;
  }
  * { box-sizing: border-box; margin: 0; padding: 0; }
  html, body { width: 1200px; height: 873px; overflow: hidden; }
  body {
    background: var(--stage);
    font-family: "Roboto", Arial, sans-serif;
    position: relative;
  }
  .card {
    position: absolute;
    top: 271px;
    width: 510px;
    height: 330px;
    box-shadow: 0 2px 10px rgba(0,0,0,0.12);
  }
  .card--front { left: 60px; background: var(--card-white); }
  .card--back { left: 630px; background: var(--lime); }

  .identity { position: absolute; left: 40px; top: 34px; }
  .identity__mark {
    width: 14px; height: 14px; border-radius: 50%;
    border: 2px solid var(--leaf); margin-bottom: 8px;
  }
  .identity__name { color: var(--name-blue); font-size: 18px; font-weight: 400; line-height: 22px; }
  .identity__role { color: var(--muted); font-size: 11px; font-style: italic; margin-top: 3px; }

  .brand {
    position: absolute;
    display: flex; align-items: center; gap: 10px;
    font-size: 22px; font-weight: 500; color: var(--leaf);
    white-space: nowrap;
  }
  .brand__dot { width: 34px; height: 34px; border-radius: 50%; flex: none; }
  .card--front .brand { left: 260px; top: 100px; }
  .card--front .brand__dot { background: var(--lime-soft); }
  .card--back .brand { left: 50%; top: 50%; transform: translate(-50%, -50%); font-size: 30px; }
  .card--back .brand__dot { width: 46px; height: 46px; background: var(--leaf); }

  .contacts {
    position: absolute; right: 22px; top: 192px;
    list-style: none; display: flex; flex-direction: column; gap: 12px;
  }
  .contacts__item {
    display: flex; justify-content: flex-end; align-items: center; gap: 10px;
    color: var(--ink); font-size: 14px; line-height: 18px; white-space: nowrap;
  }
  .contacts__icon { width: 14px; height: 14px; flex: none; }
</style>
</head>
<body>
  <section class="card card--front">
    <div class="identity">
      <div class="identity__mark"></div>
      <h1 class="identity__name">Dr. Mareike Venhaus</h1>
      <p class="identity__role">Commercial Expert</p>
    </div>

    <div class="brand"><span class="brand__dot"></span>Venhaus</div>

    <ul class="contacts">
      <li class="contacts__item">01762290471
        <svg class="contacts__icon" viewBox="0 0 14 14" fill="none" stroke="var(--icon)" stroke-width="1.4">
          <path d="M3 1.5l2 3-1.2 1.2c.8 1.6 1.9 2.7 3.5 3.5L8.5 8l3 2-1 2.5C6 12 2 8 1.5 3.5z"/>
        </svg>
      </li>
      <li class="contacts__item">Tulpenau 9, 24519 Birkenfelde
        <svg class="contacts__icon" viewBox="0 0 14 14" fill="none" stroke="var(--icon)" stroke-width="1.4">
          <path d="M7 13s-4-4.5-4-7.5a4 4 0 018 0C11 8.5 7 13 7 13z"/><circle cx="7" cy="5.5" r="1.5"/>
        </svg>
      </li>
      <li class="contacts__item">https://www.netzvelo-profil.de/profile/Mareike_Venhaus/
        <svg class="contacts__icon" viewBox="0 0 14 14" fill="none" stroke="var(--icon)" stroke-width="1.4">
          <circle cx="7" cy="7" r="5.8"/><path d="M1.2 7h11.6M7 1.2c2.2 2.4 2.2 9.2 0 11.6M7 1.2c-2.2 2.4-2.2 9.2 0 11.6"/>
        </svg>
      </li>
    </ul>
  </section>

  <section class="card card--back">
    <div class="brand"><span class="brand__dot"></span>Venhaus</div>
  </section>
</body>
</html>
```